New Flyer Design Project

I need to make a flyer with the dishes I make
With a fixed price zone, phone number 0648352917, Facebook: Tia Marilse Filipino Food

Target Market(s)

Customers of open-air markets, individuals, and special orders

Industry/Entity Type

Food truck

Font styles to use
Decorative
Script

```html
<!DOCTYPE html>
<html lang="en">
<head>
<meta charset="utf-8">
<title>Tia Marilse Filipino Food – Flyer</title>
<link href="https://fonts.googleapis.com/css2?family=Montserrat:wght@500;700;800;900&family=Kaushan+Script&display=swap" rel="stylesheet">
<style>
  :root{
    --backdrop:#d9d9d9;
    --ink:#141414;
    --ink-soft:#222;
    --white:#ffffff;
    --orange:#f39a1e;
    --red:#e0231c;
    --muted:#bdbdbd;
    --food-dark:#5a2412;
    --food-warm:#b8561f;
    --leaf:#3f8f2a;
  }
  *{margin:0;padding:0;box-sizing:border-box}
  html,body{width:1200px;height:2292px;overflow:hidden;background:var(--backdrop)}
  body{position:relative;font-family:'Montserrat',sans-serif;color:var(--white)}
  .page{position:absolute;left:200px;width:800px;height:1131px;overflow:hidden;
    background:radial-gradient(ellipse at 50% 40%,var(--ink-soft),var(--ink) 70%);}
  .page--front{top:10px}
  .page--back{top:1151px}
  .abs{position:absolute}
  .brand{display:flex;align-items:center;gap:10px;font-weight:800;font-size:22px;color:var(--orange);letter-spacing:.5px}
  .brand-dot{width:22px;height:22px;border-radius:50%;background:var(--orange)}
  .script{font-family:'Kaushan Script',cursive}
  .photo{position:absolute}
  /* front */
  .front-brand{top:60px;left:0;width:100%;justify-content:center}
  .headline{top:250px;width:100%;text-align:center;line-height:1}
  .headline .super{font-weight:900;font-size:62px;letter-spacing:1px}
  .headline .delicious{font-size:76px;color:var(--orange);margin-left:8px}
  .headline .menu{display:block;font-weight:900;font-size:72px;margin-top:6px;letter-spacing:1px}
  .plate{left:120px;top:440px;width:560px;height:330px;border-radius:50%;
    background:radial-gradient(ellipse at 50% 45%,var(--food-warm),var(--food-dark) 60%,#1b1b1b 72%,#333 100%)}
  .rolls{left:640px;top:360px;width:120px;height:150px;border-radius:18px;
    background:linear-gradient(160deg,#f0b64a,#c77a1c)}
  .leaf{left:-30px;top:700px;width:170px;height:110px;border-radius:50%;
    background:linear-gradient(120deg,var(--leaf),#1f5416);transform:rotate(-25deg)}
  .swoosh{left:0;top:640px;width:800px;height:220px}
  .order{top:850px;width:100%;text-align:center}
  .order .script{font-size:48px;color:var(--orange);display:block}
  .phone{font-weight:900;font-size:66px;letter-spacing:2px;display:block;margin-top:4px}
  .social{display:flex;justify-content:center;align-items:center;gap:10px;font-size:18px;font-weight:600;margin-top:14px}
  .social-dot{width:20px;height:20px;border-radius:50%;background:var(--white)}
  .site{font-size:16px;color:var(--muted);margin-top:12px;display:block}
  /* back */
  .back-title{left:50px;top:50px;font-weight:900;font-size:46px;color:var(--orange)}
  .back-rule{left:50px;top:112px;width:430px;height:6px;background:var(--red)}
  .section{left:50px;font-size:46px}
  .items{left:50px;list-style:none;width:480px}
  .items li{display:flex;align-items:baseline;gap:10px;font-size:22px;font-weight:700;margin-bottom:30px}
  .items .name{color:var(--orange)}
  .items .leader{flex:1;border-bottom:2px dotted var(--muted)}
  .items .price{color:var(--white)}
  .dish{left:590px;width:150px;height:150px;border-radius:50%;border:6px solid var(--orange);
    background:radial-gradient(circle at 45% 40%,var(--food-warm),var(--food-dark) 75%)}
  .back-brand{left:520px;top:840px}
  .back-photo{left:-40px;top:920px;width:300px;height:240px;border-radius:50%;
    background:radial-gradient(ellipse at 55% 45%,var(--food-warm),var(--food-dark) 70%)}
  .back-order{right:50px;top:930px;text-align:right}
  .back-order .script{font-size:40px;color:var(--orange);display:block}
  .back-order .phone{font-size:54px}
  .bottom-band{left:0;bottom:0;width:100%;height:16px;background:linear-gradient(90deg,var(--red),var(--orange))}
</style>
</head>
<body>

<section class="page page--front">
  <div class="abs brand front-brand"><span class="brand-dot"></span>Tia Marilse Filipino Food</div>
  <h1 class="abs headline"><span class="super">SUPER</span><span class="delicious script">Delicious</span><span class="menu">FOOD MENU</span></h1>
  <svg class="abs swoosh" viewBox="0 0 800 220" aria-hidden="true">
    <path d="M60 60 Q400 250 760 40 Q400 200 60 60Z" fill="var(--red)"/>
    <path d="M90 80 Q400 230 730 70" fill="none" stroke="var(--orange)" stroke-width="6"/>
  </svg>
  <div class="photo plate" role="img" aria-label="Plate of Filipino stir-fried pork dish"></div>
  <div class="photo rolls" role="img" aria-label="Crispy spring rolls"></div>
  <div class="photo leaf" role="img" aria-label="Green leaf garnish"></div>
  <div class="abs order">
    <span class="script">Order now!</span>
    <span class="phone">0648352917</span>
    <div class="social"><span class="social-dot"></span>Tia Marilse Filipino Food</div>
    <span class="site">www.tiamarilsefood.com</span>
  </div>
</section>

<section class="page page--back">
  <h2 class="abs back-title">OUR SPECIAL MENU</h2>
  <div class="abs back-rule"></div>

  <h3 class="abs section script" style="top:140px">Main Dishes</h3>
  <ul class="abs items" style="top:230px">
    <li><span class="name">Pork Adobo</span><span class="leader"></span><span class="price">$8</span></li>
    <li><span class="name">Chicken Inasal</span><span class="leader"></span><span class="price">$9</span></li>
    <li><span class="name">Beef Kaldereta</span><span class="leader"></span><span class="price">$10</span></li>
    <li><span class="name">Pancit Canton</span><span class="leader"></span><span class="price">$7</span></li>
  </ul>

  <h3 class="abs section script" style="top:520px">Beverages</h3>
  <ul class="abs items" style="top:610px">
    <li><span class="name">Buko Juice</span><span class="leader"></span><span class="price">$3</span></li>
    <li><span class="name">Calamansi Cooler</span><span class="leader"></span><span class="price">$3</span></li>
    <li><span class="name">Sago Gulaman</span><span class="leader"></span><span class="price">$4</span></li>
  </ul>

  <div class="photo dish" style="top:150px" role="img" aria-label="Filipino meat dish"></div>
  <div class="photo dish" style="top:320px" role="img" aria-label="Braised beef stew"></div>
  <div class="photo dish" style="top:490px" role="img" aria-label="Fried noodle dish"></div>
  <div class="photo dish" style="top:660px" role="img" aria-label="Fried rice plate"></div>

  <div class="abs brand back-brand"><span class="brand-dot"></span>Tia Marilse Filipino Food</div>

  <div class="photo back-photo" role="img" aria-label="Bowl of Filipino food"></div>
  <div class="abs back-order">
    <span class="script">Order now!</span>
    <span class="phone">0648352917</span>
  </div>
  <div class="abs bottom-band"></div>
</section>

</body>
</html>
```